Wexmoor Capital Lettehead project

we need letterhead for a new company in NJ called Wexmoor Capital, llc. We finance sub-prime auto loans from all over the US. We'd like to see letterhead that incorporates the logo we recently had designed on
Draftwell. The final design should have a rich and traditional look to it

Target Market(s)

Traditional Investment Banks in the US & Europe

Industry/Entity Type

Finance

Font styles to use
Other font styles liked:
• Centaur, Times New Roman, Serif

Requirements
Must have
• Our logo and the address & contact info for both our locations:
• 7 Larkspur Ave, Suite 248, Halvern Falls, NJ 07715 - Dealer Relations - Portfolio Development
• 418 Marlow Road, Corwin Township, NJ 07934 - Investor Relations - Portfolio Mgmt
• T: 555.555.0142 F: 555.555.0187

```html
<!DOCTYPE html>
<html lang="en">
<head>
<meta charset="utf-8">
<title>Wexmoor Capital, llc — Letterhead</title>
<link rel="stylesheet" href="https://fonts.googleapis.com/css2?family=Source+Sans+3:wght@400&family=Tinos:wght@400&display=swap">
<style>
  :root {
    --backdrop: #e4e4e4;
    --paper: #efeff0;
    --ink: #1f1f1f;
    --brand-ink: #2a2a2a;
    --brand-dot: #5c5c5c;
    --signature: #9fb0cc;
  }
  * { margin: 0; padding: 0; box-sizing: border-box; }
  html, body {
    width: 923px; height: 1200px; overflow: hidden;
    background: var(--backdrop);
  }
  .letterhead {
    position: absolute; left: 91px; top: 58px;
    width: 766px; height: 1085px;
    background: var(--paper);
    color: var(--ink);
  }
  .brand {
    position: absolute; left: 30px; top: 80px;
    display: flex; align-items: center;
  }
  .brand-dot {
    width: 22px; height: 22px; border-radius: 50%;
    background: var(--brand-dot);
  }
  .brand-name {
    margin-left: 12px;
    font-family: "Tinos", "Times New Roman", serif;
    font-size: 26px; letter-spacing: 0.5px;
    color: var(--brand-ink);
  }
  .letter {
    position: absolute; left: 111px; top: 297px; width: 544px;
    font-family: "Source Sans 3", "Myriad Pro", sans-serif;
  }
  .salutation { font-size: 22px; line-height: 28px; margin-bottom: 34px; font-weight: 400; }
  .letter p {
    font-size: 13px; letter-spacing: 0.1px; line-height: 19.6px;
    text-align: justify; margin-bottom: 19.6px;
  }
  .signature {
    position: absolute; left: 484px; top: 728px;
    width: 156px; height: 64px; border-radius: 30px;
    background: radial-gradient(ellipse at center, var(--signature) 0%, rgba(159,176,204,0.25) 60%, rgba(159,176,204,0) 75%);
    opacity: 0.7;
  }
  .closing {
    position: absolute; left: 579px; top: 743px;
    font-family: "Source Sans 3", "Myriad Pro", sans-serif;
    font-size: 11px;
  }
  .contact {
    position: absolute;
    font-family: "Tinos", "Times New Roman", serif;
    font-style: normal;
    font-size: 12.4px; line-height: 14.4px;
    color: #000;
  }
  .office-primary { left: 28px; top: 1009px; }
  .phone-lines { left: 341px; top: 1039px; }
  .office-secondary { left: 633px; top: 993px; }
</style>
</head>
<body>
  <main class="letterhead">
    <header class="brand">
      <div class="brand-dot"></div>
      <div class="brand-name">Wexmoor Capital, llc</div>
    </header>

    <section class="letter">
      <h1 class="salutation">Dear Mr. Smith,</h1>
      <p>Lorem ipsum dolor sit amet, consectetur adipiscing elit. Donec orci purus, luctus vitae dignissim eu, iaculis sed purus. Vivamus faucibus, ipsum nec aliquet viverra, leo mauris condimentum ligula, sit amet sagittis enim ligula quis arcu. Nam egestas tortor id nisi porttitor mattis. In tortor ante, ultricies in suscipit a, tempus non massa. Vivamus et auctor mi. Fusce vel massa nulla. Phasellus nec eros mauris, et scelerisque orci.</p>
      <p>Donec malesuada orci vitae nulla accumsan porta a id massa. Quisque accumsan iaculis magna sit amet fringilla. Maecenas consequat, magna eget tincidunt semper, odio nibh rutrum mi, id feugiat ante nisi eu risus. Vestibulum nunc orci, rhoncus a placerat in, ultricies in mi. Cras mattis varius eros, vel fringilla nisi suscipit eget. Quisque scelerisque sagittis nulla at porttitor.</p>
      <p>Sed id augue vitae urna euismod commodo aliquet a quam. Pellentesque arcu velit, cursus et malesuada ut, consequat et diam. Nullam erat sem, rhoncus id ullamcorper vitae, rhoncus et arcu. In ultricies ultricies nulla, ut rutrum nisi iaculis at. Donec eu magna a metus ornare faucibus. Fusce aliquet faucibus ultricies. Morbi semper, est id tincidunt gravida, sem arcu adipiscing lacus, ac bibendum nulla leo eu purus. Quisque nec diam sed risus consectetur a ccumsan quis quis nibh. Vestibulum id purus lorem.</p>
    </section>

    <div class="signature" role="img" aria-label="Handwritten signature of the sender"></div>
    <div class="closing">Sincerely,</div>

    <footer>
      <address class="contact office-primary">
        7 Larkspur Ave, Suite 248<br>Halvern Falls, NJ 07715<br>Dealer Relations<br>Portfolio Development
      </address>
      <div class="contact phone-lines">T: 555.555.0142<br>F: 555.555.0187</div>
      <address class="contact office-secondary">
        418 Marlow Road,<br>Corwin Township,<br>NJ 07934<br>Investor Relations<br>Portfolio Mgmt
      </address>
    </footer>
  </main>
</body>
</html>
```